Private Gym Needs a Rack Card Design

We need a basic front and back rack card (same size as post card) that gives basic information about our brand, and includes our logo. Please see attached logo and required content below.

Target Market(s)

Upscale, private gym.

Industry/Entity Type

Gym

Font styles to use
Sans Serif

Colors
ffffff
5c5c5c
000000
dbdbdb
f78f20

Requirements
Must have
• Business Logo and the following text in a clean, modern, easy-to-read, artistic manner. Style and design must be clean, incorporate our color scheme of MOSTLY white, light grey, charcoal, with just pops of orange. We want the card itself to be mostly white background. Must include website URL as well: corevantagestudio.com
• FRONT CARD:
• Logo
• A safe and individualized approach to exercise
• Our method employs the latest weight resistance training exercises and coaching for healthy living. Not only is our workout methodology effective, it’s safe.
• Our Method…
• -Improves Functional Movement
• -Promotes Weight Loss
• -Builds Strength
• -Increases Flexibility 

• BACK:
• Change Your Body. Find Your Strength.
• There’s 40 years of success behind our proven method
• What is The Formwell? 
• The Formwell is all about teaching our clients how to lift weights and exercise with the proper technique. There’s no slinging or jerking at our gym; only controlled movements that yield real results.
• Come workout with us in our private gym. We are located in Durham adjacent to Harlow Campus and 5 minutes from downtown Durham.
• Address: 482 Linden Ave, Durham, NC 27705
• Phone: (919) 555-2741
• Hours: 9:00 AM – 9:00 PM
Nice to have
• Great organization of text, maybe some columns, colored bullet points, cool graphics and logos.
Should not have
• Busy or crowded design. All lines should be sleek, straight, and streamline. NO STOCK IMAGES, but logos are GREAT

```html
<!DOCTYPE html>
<html lang="en">
<head>
<meta charset="utf-8">
<title>The Formwell — Rack Card Front</title>
<link rel="stylesheet" href="https://fonts.googleapis.com/css2?family=Questrial&display=swap">
<style>
  :root {
    --white: #ffffff;
    --charcoal: #5f5f61;
    --graphite: #666668;
    --ink: #000000;
    --night: #222222;
    --panel: #c0c0c0;
    --silver: #bfbfbf;
    --ember: #f06533;
    --tangerine: #f59222;
  }
  * { margin: 0; padding: 0; box-sizing: border-box; }
  html, body {
    width: 1200px;
    height: 857px;
    overflow: hidden;
    background: var(--white);
  }
  .card {
    position: relative;
    width: 1200px;
    height: 857px;
    background: var(--white);
    font-family: "Questrial", sans-serif;
    color: var(--ink);
  }
  .brand {
    position: absolute;
    left: 0;
    right: 0;
    top: 40px;
    display: flex;
    justify-content: center;
    align-items: center;
    gap: 18px;
  }
  .brand-mark {
    width: 34px;
    height: 34px;
    background: var(--ember);
  }
  .brand-name {
    font-size: 72px;
    line-height: 1;
    color: var(--charcoal);
    letter-spacing: 1px;
  }
  .tagline-band {
    position: absolute;
    left: 0;
    top: 180px;
    width: 1200px;
    height: 76px;
    background: var(--charcoal);
    color: var(--white);
    font-size: 48px;
    line-height: 76px;
    padding-left: 44px;
    white-space: nowrap;
  }
  .info-panel {
    position: absolute;
    left: 0;
    top: 272px;
    width: 812px;
    height: 585px;
    background: var(--panel);
  }
  .intro {
    position: absolute;
    left: 24px;
    top: 12px;
    width: 760px;
    font-size: 39px;
    line-height: 51px;
  }
  .intro span { display: block; white-space: nowrap; }
  .intro .indent { padding-left: 11px; }
  .method-title {
    position: absolute;
    right: 40px;
    top: 280px;
    font-size: 64px;
    line-height: 1;
    color: var(--ember);
  }
  .benefits {
    position: absolute;
    right: 38px;
    top: 350px;
    list-style: none;
    text-align: right;
    color: var(--white);
    font-size: 44px;
    line-height: 54.5px;
  }
  .accent-bars { position: absolute; left: 0; top: 0; }
</style>
</head>
<body>
  <main class="card">
    <header class="brand">
      <span class="brand-mark"></span>
      <span class="brand-name">The Formwell</span>
    </header>

    <h1 class="tagline-band">A safe and individualized approach to exercise</h1>

    <section class="info-panel">
      <p class="intro">
        <span class="indent">Our method employs the latest</span>
        <span>weight resistance training exercises</span>
        <span>and coaching for healthy living.</span>
        <span>Not only is our workout methodology</span>
        <span class="indent">effective, it’s safe.</span>
      </p>
      <h2 class="method-title">Our Method:</h2>
      <ul class="benefits">
        <li>Improves Functional Movement</li>
        <li>Promotes Weight Loss</li>
        <li>Builds Strength</li>
        <li>Increases Flexibility</li>
      </ul>
    </section>

    <svg class="accent-bars" width="1200" height="857" viewBox="0 0 1200 857" aria-hidden="true">
      <rect x="950" y="338" width="250" height="56" fill="var(--graphite)"/>
      <rect x="884" y="414" width="316" height="44" fill="var(--night)"/>
      <rect x="1005" y="474" width="195" height="48" fill="var(--ember)"/>
      <rect x="888" y="542" width="312" height="28" fill="var(--silver)"/>
      <rect x="960" y="590" width="240" height="50" fill="var(--tangerine)"/>
      <rect x="904" y="662" width="296" height="54" fill="var(--graphite)"/>
      <rect x="963" y="734" width="237" height="44" fill="var(--night)"/>
    </svg>
  </main>
</body>
</html>
```